New Business Card Design Project

Bloom of the Willow Wellness Clinic PLLC
Bloomofthewillowwc-example.com
Board Certified Nursing Coach in life, health, & wellness.
Hypnotherapy, weight loss & vitamin supplement injections, IV hydration.
Offering mobile clinics

```html
<!DOCTYPE html>
<html lang="en">
<head>
<meta charset="utf-8">
<title>Bloom of the Willow Wellness Clinic – Business Cards</title>
<link rel="stylesheet" href="https://fonts.googleapis.com/css2?family=Lato:wght@400;700&display=swap">
<style>
  :root {
    --stage: #222222;
    --card: #5a2f31;
    --cream: #f4e9dc;
    --orange: #f08a1c;
    --line: #e9ddd0;
  }
  * { box-sizing: border-box; margin: 0; padding: 0; }
  html, body { width: 1200px; height: 900px; overflow: hidden; }
  body {
    background: var(--stage);
    font-family: "Lato", sans-serif;
    position: relative;
  }
  .card {
    position: absolute;
    left: 290px;
    width: 620px;
    height: 354px;
    background: var(--card);
    border-radius: 24px;
    color: var(--cream);
  }
  .card--front { top: 60px; }
  .card--back { top: 470px; }

  .accent {
    position: absolute;
    height: 2px;
    width: 70px;
    background: linear-gradient(90deg, transparent, var(--orange), transparent);
  }

  /* front */
  .front-mark {
    position: absolute;
    left: 50%; top: 40px;
    width: 92px; height: 92px;
    margin-left: -46px;
    border-radius: 50%;
    background: var(--orange);
  }
  .front-name {
    position: absolute;
    left: 0; right: 0; top: 152px;
    text-align: center;
    font-weight: 700;
    font-size: 30px;
    letter-spacing: 3px;
    text-transform: uppercase;
    line-height: 1.25;
  }
  .front-name .sub { display: block; font-size: 16px; letter-spacing: 4px; }
  .front-services {
    position: absolute;
    left: 40px; right: 40px; top: 258px;
    text-align: center;
    font-size: 15px;
    line-height: 1.4;
  }

  /* back */
  .back-mark {
    position: absolute;
    left: 46px; top: 44px;
    width: 80px; height: 80px;
    border-radius: 50%;
    background: var(--orange);
  }
  .back-name {
    position: absolute;
    left: 150px; top: 36px;
    font-weight: 700;
    font-size: 27px;
    letter-spacing: 3px;
    text-transform: uppercase;
    line-height: 1.25;
  }
  .back-name .sub { display: block; font-size: 14px; letter-spacing: 4px; padding-left: 80px; }
  .divider {
    position: absolute;
    height: 1px;
    background: var(--line);
  }
  .person {
    position: absolute;
    left: 46px; top: 154px;
  }
  .person-name {
    font-size: 24px;
    font-weight: 700;
    color: var(--orange);
    text-transform: uppercase;
  }
  .person-title { font-size: 15px; margin-top: 2px; }
  .contacts {
    position: absolute;
    left: 46px; top: 236px;
    list-style: none;
    font-size: 15px;
  }
  .contacts li { display: flex; align-items: center; gap: 12px; height: 28px; }
  .contacts svg { width: 16px; height: 16px; flex: none; }
  .address {
    position: absolute;
    right: 46px; top: 250px;
    text-align: right;
    font-size: 15px;
    line-height: 1.45;
  }
</style>
</head>
<body>

<section class="card card--front">
  <div class="front-mark"></div>
  <h1 class="front-name">Bloom of the Willow<span class="sub">Wellness Clinic</span></h1>
  <span class="accent" style="left:90px; top:236px;"></span>
  <span class="accent" style="right:90px; top:236px;"></span>
  <p class="front-services">Hypnotherapy, Weight loss &amp; Vitamin Supplement Injections,<br>IV hydration. Offering mobile clinics</p>
</section>

<section class="card card--back">
  <div class="back-mark"></div>
  <h2 class="back-name">Bloom of the Willow<span class="sub">Wellness Clinic</span></h2>
  <span class="accent" style="left:150px; top:112px;"></span>
  <span class="accent" style="right:46px; top:82px;"></span>
  <div class="divider" style="top:134px; left:300px; right:46px;"></div>
  <div class="person">
    <p class="person-name">Daniel Carter</p>
    <p class="person-title">Board Certified Nursing Coach in life, health, &amp; wellness.</p>
  </div>
  <div class="divider" style="top:222px; left:46px; right:300px;"></div>
  <ul class="contacts">
    <li><svg viewBox="0 0 16 16"><path d="M3 1l3 3-1.5 2a9 9 0 0 0 5.5 5.5L12 10l3 3-2 2C7 15 1 9 1 3z" fill="#f08a1c"/></svg>044-987 654 321</li>
    <li><svg viewBox="0 0 16 16"><path d="M1 3h14v10H1z M1 3l7 6 7-6" fill="none" stroke="#f08a1c" stroke-width="1.6"/></svg>info@bloomwillow-example.com</li>
    <li><svg viewBox="0 0 16 16"><circle cx="8" cy="8" r="7" fill="none" stroke="#f08a1c" stroke-width="1.6"/><path d="M1 8h14M8 1c-3 4-3 10 0 14M8 1c3 4 3 10 0 14" fill="none" stroke="#f08a1c" stroke-width="1.2"/></svg>www.Bloomofthewillowwc-example.com</li>
  </ul>
  <p class="address">421, Address line goes here<br>45452, Country name</p>
</section>

</body>
</html>
```